Heron Renovation Group Postcard Design Project

I'm a General Contractor specializing in luxury residential remodeling.

THIS IS AN EDDM POSTCARD. THE ENTIRE BACK SIDE OF THE CARD WILL BE USED.

I FORGOT TO MENTION THIS IN MY ORIGINAL BRIEF.

Target Market(s)

OLD, rich people so please make sure the fonts are clear and crisp.

Font styles to use
Sans Serif

```html
<!DOCTYPE html>
<html lang="en">
<head>
<meta charset="utf-8">
<title>Heron Renovation Group – EDDM Postcard</title>
<link rel="stylesheet" href="https://fonts.googleapis.com/css2?family=Catamaran:wght@500;600;700;800&display=swap">
<style>
  :root {
    --page: #8a8a8a;
    --red: #e3211c;
    --charcoal: #3f3f3f;
    --ink: #1f1f1f;
    --white: #ffffff;
    --mist: #d9e3e7;
    --sky: #e3f0f3;
    --stamp: #e6e6e6;
    --rule: #777777;
    --teal: #6cc5cf;
    --blue: #3aa6dc;
    --navy: #2a5a85;
    --plum: #8c2b47;
    --rose: #e04a55;
    --orange: #f08a2c;
    --gold: #f2c230;
  }
  * { margin: 0; padding: 0; box-sizing: border-box; }
  html, body { width: 720px; height: 1200px; overflow: hidden; }
  body {
    position: relative;
    background: var(--page);
    font-family: "Catamaran", sans-serif;
    color: var(--ink);
  }
  .card { position: absolute; overflow: hidden; background: var(--white); }
  .card svg.shapes { position: absolute; inset: 0; }
  .text { position: absolute; left: 0; right: 0; text-align: center; }

  /* Front */
  .card-front { left: 145px; top: 64px; width: 431px; height: 638px; }
  .brand {
    position: absolute; left: 0; right: 0; top: 160px;
    display: flex; justify-content: center; align-items: center; gap: 8px;
    font-size: 21px; font-weight: 800; color: var(--ink); letter-spacing: .2px;
  }
  .brand-mark { width: 14px; height: 14px; background: var(--red); }
  .tagline { top: 212px; font-size: 19px; font-weight: 700; line-height: 23px; color: var(--ink); }
  .contractor {
    position: absolute; left: 78px; top: 282px; width: 276px; height: 28px;
    background: var(--red); color: var(--white);
    font-size: 15px; font-weight: 600; line-height: 29px; text-align: center;
  }
  .services { top: 393px; font-size: 17.5px; font-weight: 600; line-height: 21.5px; color: var(--white); }
  .license { top: 480px; font-size: 17.5px; font-weight: 600; color: var(--white); }
  .front-phone { top: 561px; font-size: 21px; font-weight: 700; color: var(--white); letter-spacing: .5px; }
  .front-web { top: 588px; font-size: 18.5px; font-weight: 700; color: var(--white); }

  /* Back */
  .card-back { left: 63px; top: 750px; width: 595px; height: 402px; }
  .values-chart { position: absolute; left: 0; top: 0; }
  .chart-label { font-family: "Catamaran", sans-serif; font-size: 10px; font-weight: 600; fill: var(--white); }
  .core-title { font-family: "Catamaran", sans-serif; font-size: 12px; font-weight: 800; fill: var(--ink); }
  .back-brand {
    position: absolute; display: flex; align-items: center; gap: 4px;
    font-size: 9px; font-weight: 800; color: var(--ink); white-space: nowrap;
  }
  .back-brand .brand-mark { width: 7px; height: 7px; }
  .back-brand-chart { left: 120px; top: 276px; }
  .back-brand-mail { left: 455px; top: 164px; }
  .back-phone {
    position: absolute; left: 0; width: 310px; top: 310px; text-align: center;
    font-size: 29px; font-weight: 800; color: var(--white); letter-spacing: .5px;
  }
  .back-web {
    position: absolute; left: 0; width: 310px; top: 348px; text-align: center;
    font-size: 14px; font-weight: 700; color: var(--white);
  }
  .stamp { position: absolute; left: 474px; top: 35px; width: 85px; height: 86px; background: var(--stamp); }
  .address-line { position: absolute; left: 390px; width: 169px; height: 1px; background: var(--rule); }
</style>
</head>
<body>

<section class="card card-front" aria-label="Postcard front">
  <svg class="shapes" width="431" height="638" viewBox="0 0 431 638">
    <defs>
      <linearGradient id="blueprintTone" x1="0" y1="0" x2="1" y2="1">
        <stop offset="0" stop-color="#eef4f6"/>
        <stop offset="1" stop-color="#c9dbe2"/>
      </linearGradient>
    </defs>
    <rect x="0" y="0" width="431" height="390" fill="url(#blueprintTone)" role="img" aria-label="Photo of rolled architectural blueprints with a pen and ruler"/>
    <polygon points="170,375 431,322 431,352" fill="var(--red)"/>
    <polygon points="0,380 431,352 431,510 0,548" fill="var(--charcoal)"/>
    <polygon points="0,548 330,520 0,568" fill="var(--mist)"/>
    <polygon points="0,568 431,510 431,638 0,638" fill="var(--red)"/>
  </svg>

  <div class="brand"><span class="brand-mark"></span>Heron Renovation Group</div>
  <p class="text tagline">Remodeling Luxury Homes &amp; Building<br>Lasting Relationships Since 1995</p>
  <p class="contractor">Marcus Hale, General Contractor</p>
  <p class="text services">All Phases of Residential Remodeling<br>Partial &amp; Large Scale Renovations<br>Complimentary Design Services</p>
  <p class="text license">Licensed / Bonded / Insured #518374</p>
  <p class="text front-phone">480-555-0142</p>
  <p class="text front-web">www.HeronRenovationGroup.com</p>
</section>

<section class="card card-back" aria-label="Postcard back">
  <svg class="shapes" width="595" height="402" viewBox="0 0 595 402">
    <polygon points="0,0 401,0 297,402 0,402" fill="var(--sky)"/>
    <polygon points="397,0 404,0 329,402 297,402" fill="var(--ink)"/>
    <polygon points="0,305 316,305 300,378 0,378" fill="var(--red)"/>
  </svg>

  <svg class="values-chart" width="360" height="300" viewBox="0 0 360 300" aria-label="Core values chart">
    <g stroke="var(--sky)" stroke-width="3">
      <path d="M95.6,225.4 A118,118 0 0 1 61,142 L117,142 A62,62 0 0 0 135.2,185.8 Z" fill="var(--teal)"/>
      <path d="M61,142 A118,118 0 0 1 95.6,58.6 L135.2,98.2 A62,62 0 0 0 117,142 Z" fill="var(--blue)"/>
      <path d="M95.6,58.6 A118,118 0 0 1 179,24 L179,80 A62,62 0 0 0 135.2,98.2 Z" fill="var(--navy)"/>
      <path d="M179,24 A118,118 0 0 1 262.4,58.6 L222.8,98.2 A62,62 0 0 0 179,80 Z" fill="var(--plum)"/>
      <path d="M262.4,58.6 A118,118 0 0 1 297,142 L241,142 A62,62 0 0 0 222.8,98.2 Z" fill="var(--rose)"/>
      <path d="M297,142 A118,118 0 0 1 262.4,225.4 L222.8,185.8 A62,62 0 0 0 241,142 Z" fill="var(--orange)"/>
    </g>
    <text class="chart-label" text-anchor="middle"><tspan x="94" y="156">World</tspan><tspan x="94" y="167">Class</tspan><tspan x="94" y="178">Customer</tspan><tspan x="94" y="189">Service</tspan></text>
    <text class="chart-label" text-anchor="middle" x="94" y="111">Integrity</text>
    <text class="chart-label" text-anchor="middle"><tspan x="146" y="55">The Creative</tspan><tspan x="146" y="66">Process</tspan></text>
    <text class="chart-label" text-anchor="middle"><tspan x="215" y="55">Educating</tspan><tspan x="215" y="66">Our Clients</tspan></text>
    <text class="chart-label" text-anchor="middle"><tspan x="264" y="106">Having</tspan><tspan x="264" y="117">Fun</tspan></text>
    <text class="chart-label" text-anchor="middle"><tspan x="264" y="168">Quality</tspan><tspan x="264" y="179">Craftsm-</tspan><tspan x="264" y="190">anship</tspan></text>

    <rect x="148" y="100" width="62" height="156" rx="28" fill="var(--gold)" role="img" aria-label="Illustration of a light bulb lifting off like a rocket"/>
    <text class="core-title" text-anchor="middle"><tspan x="179" y="130">CORE</tspan><tspan x="179" y="143">VALUES</tspan></text>
  </svg>

  <div class="back-brand back-brand-chart"><span class="brand-mark"></span>Heron Renovation Group</div>
  <p class="back-phone">480-555-0142</p>
  <p class="back-web">www.HeronRenovationGroup.com</p>

  <div class="stamp" aria-label="Postage area"></div>
  <div class="back-brand back-brand-mail"><span class="brand-mark"></span>Heron Renovation Group</div>
  <div class="address-line" style="top:247px"></div>
  <div class="address-line" style="top:279px"></div>
  <div class="address-line" style="top:312px"></div>
</section>

</body>
</html>
```